Business Card Design Project

Business Card
We are rebranding with a new logo
Industry/Entity Type
Business
Contact Information for Business Card
Dennis Marlow +61 427581962 dennis@qovo.com.au P.O. Box 872 Kelvindale QLD 4309
Requirements
Must have
- Logo

```html
<!DOCTYPE html>
<html lang="en">
<head>
<meta charset="utf-8">
<title>Qovo International – Business Card</title>
<link href="https://fonts.googleapis.com/css2?family=Source+Sans+3:wght@400;600;700&display=swap" rel="stylesheet">
<style>
  :root {
    --page-bg: #e9eaec;
    --card-white: #ffffff;
    --card-grey: #e4e5e7;
    --ink: #111418;
    --brand-navy: #14306e;
    --band-navy: #0b1f4f;
    --band-blue: #1f5aa6;
    --accent-orange: #f29a12;
    --icon-orange: #e8731a;
  }
  html, body {
    margin: 0;
    width: 1200px;
    height: 900px;
    overflow: hidden;
    background: var(--page-bg);
    font-family: "Source Sans 3", "Myriad Pro", Arial, sans-serif;
  }
  .business-card {
    position: absolute;
    left: 100px;
    top: 165px;
    width: 1000px;
    height: 570px;
    overflow: hidden;
    background: linear-gradient(160deg, var(--card-white) 0%, #f4f4f5 45%, var(--card-grey) 100%);
    box-shadow: 0 6px 24px rgba(0,0,0,0.18);
  }
  .brand-name {
    position: absolute;
    left: 64px;
    top: 52px;
    margin: 0;
    color: var(--brand-navy);
    font-weight: 700;
    font-size: 40px;
    line-height: 1.05;
    letter-spacing: 3px;
    text-transform: uppercase;
  }
  .contact-block {
    position: absolute;
    right: 60px;
    top: 282px;
    text-align: right;
    color: var(--ink);
  }
  .contact-name {
    margin: 0 0 4px 0;
    font-size: 29px;
    font-weight: 700;
    margin-right: 36px;
  }
  .contact-line {
    display: flex;
    justify-content: flex-end;
    align-items: center;
    gap: 12px;
    font-size: 24px;
    line-height: 35px;
  }
  .contact-icon {
    width: 22px;
    height: 22px;
    flex: none;
  }
  .accent-stripe {
    position: absolute;
    left: 0;
    right: 0;
    top: 452px;
    height: 15px;
    background: linear-gradient(90deg, #e88a0c, var(--accent-orange) 60%, #f7b52a);
  }
  .base-band {
    position: absolute;
    left: 0;
    right: 0;
    top: 467px;
    bottom: 0;
    background: linear-gradient(90deg, var(--band-navy) 0%, #163c80 35%, var(--band-blue) 100%);
  }
</style>
</head>
<body>
  <div class="business-card">
    <p class="brand-name">Qovo<br>International</p>

    <div class="contact-block">
      <p class="contact-name">Dennis Marlow</p>
      <div class="contact-line">
        <span>+61 427581962</span>
        <svg class="contact-icon" viewBox="0 0 24 24" aria-hidden="true">
          <circle cx="12" cy="12" r="11" fill="var(--icon-orange)"/>
          <path d="M9 6.5c-1.6 1-2 3-1.2 5.4.9 2.6 2.9 4.9 5.3 5.7 1.3.4 2.3.1 3-.7l-2-2.1-1.4.8c-1.2-.5-2.4-2-2.9-3.4l1.3-1-1-3.3z" fill="#fff"/>
        </svg>
      </div>
      <div class="contact-line">
        <span>dennis@qovo.com.au</span>
        <svg class="contact-icon" viewBox="0 0 24 24" aria-hidden="true">
          <rect x="2" y="5" width="20" height="14" rx="1.5" fill="var(--icon-orange)"/>
          <path d="M3 6.5l9 6.5 9-6.5" stroke="#fff" stroke-width="1.6" fill="none"/>
        </svg>
      </div>
      <div class="contact-line">
        <span>P.O. Box 872 Kelvindale QLD 4309</span>
        <svg class="contact-icon" viewBox="0 0 24 24" aria-hidden="true">
          <path d="M12 1.5a7.5 7.5 0 0 0-7.5 7.5c0 5.5 7.5 13.5 7.5 13.5s7.5-8 7.5-13.5A7.5 7.5 0 0 0 12 1.5z" fill="var(--icon-orange)"/>
          <circle cx="12" cy="9" r="3" fill="#fff"/>
        </svg>
      </div>
    </div>

    <div class="accent-stripe"></div>
    <div class="base-band"></div>
  </div>
</body>
</html>
```